Website design for labour force (commercial truck driver) company

Looking for a Wordpress template (or design files in conjunction with a free Wordpress template).
Company tag line:
Tenvora – On Demand, Professional Drivers
Real Drivers | Real Standards | Real Results
Logo design has already been completed and is attached

Company provides contract drivers to trucking companies. Target market is both the trucking companies looking for drivers and drivers looking for work.
Design to encompass header / footer and basic page design, navigation menu, home page, contact page. Customer will add content and additional pages over time.

```html
<!DOCTYPE html>
<html lang="en">
<head>
<meta charset="utf-8">
<title>Tenvora – On Demand, Professional Drivers</title>
<link rel="stylesheet" href="https://fonts.googleapis.com/css2?family=Arimo:ital,wght@0,400;0,700;1,400&family=Poppins:wght@400;700&display=swap">
<style>
:root{
  --green:#187a58;
  --green-dark:#0f5a40;
  --green-light:#2aae8a;
  --ink:#111111;
  --text:#2b2b2b;
  --muted:#555;
  --white:#ffffff;
  --line:#c9c9c9;
  --footer:#0b0b0b;
}
*{box-sizing:border-box;margin:0;padding:0}
html,body{width:1200px;height:4057px;overflow:hidden}
body{position:relative;background:var(--white);font-family:"Arimo",Arial,sans-serif;color:var(--text)}
.abs{position:absolute}
.brand{font-family:"Arimo",Arial,sans-serif;font-weight:700;font-size:27px;color:var(--ink);display:flex;align-items:center;gap:10px}
.brand .dot{width:26px;height:26px;border-radius:50%;background:var(--green)}
.site-header{position:absolute;left:0;top:0;width:1200px;height:80px;background:var(--white)}
.site-header .brand{position:absolute;left:142px;top:22px}
.main-nav{position:absolute;top:31px;left:0;font-size:14px;color:var(--ink)}
.main-nav span{position:absolute;white-space:nowrap}
.main-nav .active{color:var(--green)}
.btn{display:flex;align-items:center;justify-content:center;font-weight:700;font-size:14px;border-radius:40px;text-transform:uppercase;white-space:nowrap}
.btn-green{background:var(--green);color:var(--white)}
.hero-photo{position:absolute;left:0;top:80px;width:1200px;height:560px;background:linear-gradient(100deg,#5e6466 0%,#3a3f41 35%,#252a2c 60%,#4a4a46 100%)}
.hero-panel{position:absolute;left:515px;top:192px;width:685px;height:292px;background:var(--green);border-radius:150px 0 0 150px}
.hero-title{position:absolute;left:609px;top:224px;font-family:"Poppins",sans-serif;font-size:47px;line-height:55px;color:var(--white)}
.hero-title b{font-weight:700}
.hero-text{position:absolute;left:609px;top:342px;width:440px;font-size:15px;line-height:25px;color:var(--white)}
.btn-white{background:var(--white);color:var(--ink)}
.btn-outline{border:2px solid var(--white);color:var(--white)}
.round-arrow{position:absolute;width:44px;height:44px;border-radius:50%;display:flex;align-items:center;justify-content:center}
.round-arrow.solid{background:var(--white)}
.round-arrow.line{border:1.5px solid #333;background:var(--white)}
.section-title{position:absolute;font-size:40px;color:var(--ink);font-weight:400;white-space:nowrap}
.section-title b{font-weight:700}
.rule{position:absolute;height:3px;width:63px;background:var(--green)}
.about-text{position:absolute;left:628px;width:415px;font-size:13.5px;line-height:21.5px;color:#333}
.step-card{position:absolute;top:1332px;height:350px;background:var(--green);border-radius:10px;color:var(--white);text-align:center}
.step-card.featured{background:linear-gradient(180deg,var(--green-light) 0%,#178060 45%,#0c3b29 100%);border:2px solid #0b2f21}
.step-icon{position:absolute;left:50%;top:36px;width:134px;height:134px;margin-left:-67px;border-radius:50%;background:var(--white);display:flex;align-items:center;justify-content:center}
.step-card h3{position:absolute;left:0;right:0;top:183px;font-size:18px;font-weight:700}
.step-card.featured h3{text-decoration:underline}
.step-card p{position:absolute;left:60px;right:60px;top:225px;font-size:14px;line-height:20px}
.why-item{position:absolute;left:145px;display:flex;align-items:center;gap:25px;font-size:19px;color:var(--ink)}
.tick{width:66px;height:66px;border-radius:50%;background:var(--green);display:flex;align-items:center;justify-content:center}
.photo{position:absolute;border-radius:8px}
.reviews{position:absolute;left:0;top:2321px;width:1200px;height:700px;background:linear-gradient(90deg,#1f7d5c,#238364 50%,#1f7d5c)}
.review{position:absolute;top:2487px;width:438px;height:438px;border-radius:50%;border:5px solid #c9ece0}
.review .ring{position:absolute;left:19px;top:19px;width:390px;height:390px;border-radius:50%;border:3px solid #c9ece0}
.review .card{position:absolute;left:56px;top:56px;width:316px;height:316px;border-radius:50%;background:var(--white);text-align:center}
.review .quote{position:absolute;left:0;right:0;top:30px;font-family:"Poppins",sans-serif;font-weight:700;font-size:54px;line-height:50px;color:var(--green)}
.review .stars{position:absolute;left:0;right:0;top:85px;color:#e6a01b;font-size:14px;letter-spacing:2px}
.review .msg{position:absolute;left:36px;right:36px;top:110px;font-style:italic;font-size:12.5px;line-height:20px;color:#333}
.review .name{position:absolute;left:0;right:0;top:220px;font-size:19px;color:var(--ink)}
.review .co{position:absolute;left:0;right:0;top:246px;font-size:12px;color:#555}
.field{position:absolute;border:1.5px solid #bdbdbd;border-radius:10px;padding:0 33px;font-size:16px;color:#333;display:flex;align-items:center;background:var(--white)}
.site-footer{position:absolute;left:0;top:3621px;width:1200px;height:436px;background:var(--footer);color:var(--white)}
.site-footer .brand{position:absolute;left:142px;top:89px;color:var(--white)}
.foot-nav{position:absolute;right:145px;top:96px;font-size:17px;white-space:nowrap;word-spacing:2px}
.foot-nav i{font-style:normal;margin:0 14px}
.foot-rule{position:absolute;left:142px;width:913px;height:1px;background:#3a3a3a}
.foot-head{position:absolute;top:213px;font-size:19px;font-weight:700}
.foot-line{position:absolute;left:142px;display:flex;align-items:center;gap:18px;font-size:17px}
.social{position:absolute;top:257px;width:40px;height:40px;border-radius:50%;background:var(--green)}
.newsletter{position:absolute;left:632px;top:256px;width:423px;height:53px;background:var(--white);border-radius:8px;color:#444;font-size:13px;display:flex;align-items:center;padding-left:24px}
.copyright{position:absolute;left:0;right:0;top:381px;text-align:center;font-size:15px}
</style>
</head>
<body>

<header class="site-header">
  <div class="brand"><span class="dot"></span>Tenvora</div>
  <nav class="main-nav">
    <span class="active" style="left:403px">HOME</span>
    <span style="left:479px">SERVICES</span>
    <span style="left:583px">ABOUT US</span>
    <span style="left:688px">PRICING</span>
    <span style="left:780px">CONTACT US</span>
  </nav>
  <div class="btn btn-green abs" style="left:909px;top:19px;width:146px;height:39px;font-size:13px">GET A QUOTE</div>
</header>

<section class="hero">
  <div class="hero-photo" role="img" aria-label="Truck driver leaning against the cab of a semi truck"></div>
  <div class="hero-panel"></div>
  <h1 class="hero-title"><b>Your On-Demand</b><br>Driver Workforce</h1>
  <p class="hero-text">Tenvora connects top CDL drivers with the companies that need them—fast, reliable, and fully vetted.</p>
  <div class="btn btn-white abs" style="left:609px;top:408px;width:216px;height:39px;font-size:13px">LOOKING FOR DRIVERS</div>
  <div class="btn btn-outline abs" style="left:833px;top:408px;width:216px;height:39px;font-size:13px">LOOKING FOR WORK</div>
  <div class="round-arrow solid" style="left:550px;top:556px"><svg width="12" height="12" viewBox="0 0 12 12"><path d="M8 1 3 6l5 5" fill="none" stroke="#222" stroke-width="1.6"/></svg></div>
  <div class="round-arrow solid" style="left:603px;top:556px"><svg width="12" height="12" viewBox="0 0 12 12"><path d="M4 1l5 5-5 5" fill="none" stroke="#222" stroke-width="1.6"/></svg></div>
</section>

<section class="about">
  <svg class="abs" style="left:140px;top:710px" width="444" height="444" viewBox="0 0 444 444">
    <circle cx="222" cy="222" r="217" fill="none" stroke="#0b0b0b" stroke-width="6"/>
    <circle cx="222" cy="222" r="186" fill="none" stroke="var(--green)" stroke-width="6"/>
  </svg>
  <div class="abs" role="img" aria-label="Smiling truck driver in a cap sitting at the wheel" style="left:202px;top:772px;width:320px;height:320px;border-radius:50%;background:linear-gradient(135deg,#8a8e90,#4b5052 60%,#2e3133)"></div>
  <div class="abs" style="left:432px;top:1018px;width:116px;height:116px;border-radius:50%;background:var(--white);box-shadow:0 6px 16px rgba(0,0,0,.18);display:flex;align-items:center;justify-content:center;font-weight:700;font-size:17px;color:var(--ink)">Tenvora</div>

  <h2 class="section-title" style="left:628px;top:728px"><b>About</b> Us</h2>
  <div class="rule" style="left:628px;top:782px"></div>
  <p class="about-text" style="top:806px">Lorem ipsum dolor sit amet, consectetur adipiscing elit, sed do eiusmod tempor incididunt ut labore et dolore magna aliqua. Ut enim ad minim veniam, quis nostrud exercitation ullamco labore is nisi ut aliquip ex ea commodo consequat. Duis aute irure dolor in reprehenderit in voluptate velit esse cillum dolore eu fugiat nulla pariatur. Excepteur sint occaecat cupidatat non proident, sunt in culpa qui officia deserunt mollit anim id est laborum.</p>
  <p class="about-text" style="top:979px">Lorem ipsum dolor sit amet, consectetur adipiscing elit, sed do eiusmod tempor incididunt ut labore et dolore magna aliqua. Ut enim ad minim veniam, quis nostrud exercitation ullamco labore is nisi ut aliquip ex ea commodo consequat.</p>
  <div class="btn btn-green abs" style="left:628px;top:1084px;width:147px;height:39px;font-size:13px">LEARN MORE</div>
</section>

<section class="how">
  <h2 class="section-title" style="left:0;width:1200px;text-align:center;top:1244px"><b>How It</b> Works</h2>
  <div class="rule" style="left:568px;top:1305px"></div>

  <div class="step-card" style="left:11px;width:380px">
    <div class="step-icon"><svg width="54" height="62" viewBox="0 0 54 62" fill="none" stroke="var(--green)" stroke-width="2"><rect x="8" y="3" width="34" height="56" rx="4"/><line x1="8" y1="12" x2="42" y2="12"/><line x1="8" y1="50" x2="42" y2="50"/><circle cx="25" cy="26" r="6"/><path d="M15 44c2-7 18-7 20 0"/><rect x="36" y="8" width="14" height="10" rx="2"/></svg></div>
    <h3>Post Need</h3>
    <p>Lorem ipsum dolor sit amet, consec tetur adipiscing elit, sed do eiusmod tempor incididunt ut labore et dolore magna aliqua.</p>
  </div>
  <div class="step-card featured" style="left:408px;width:384px">
    <div class="step-icon"><svg width="60" height="60" viewBox="0 0 60 60" fill="none" stroke="var(--green)" stroke-width="2"><path d="M30 14l5 10 11 2-8 8 2 11-10-5-10 5 2-11-8-8 11-2z"/><path d="M10 56l10-12M50 56L40 44"/><path d="M30 3v5M20 6l2 4M40 6l-2 4"/></svg></div>
    <h3>Get Matched</h3>
    <p>Lorem ipsum dolor sit amet, consec tetur adipiscing elit, sed do eiusmod tempor incididunt ut labore et dolore magna aliqua.</p>
  </div>
  <div class="step-card" style="left:809px;width:380px">
    <div class="step-icon"><svg width="48" height="62" viewBox="0 0 48 62" fill="none" stroke="var(--green)" stroke-width="2"><path d="M4 3h30l10 10v46H4z"/><path d="M34 3v10h10"/><rect x="10" y="20" width="6" height="6"/><rect x="10" y="32" width="6" height="6"/><rect x="10" y="44" width="6" height="6"/><path d="M21 23h16M21 35h16M21 47h16"/></svg></div>
    <h3>Drivers Report In</h3>
    <p>Lorem ipsum dolor sit amet, consec tetur adipiscing elit, sed do eiusmod tempor incididunt ut labore et dolore magna aliqua.</p>
  </div>

  <div class="round-arrow line" style="left:550px;top:1707px"><svg width="12" height="12" viewBox="0 0 12 12"><path d="M8 1 3 6l5 5" fill="none" stroke="#222" stroke-width="1.6"/></svg></div>
  <div class="round-arrow line" style="left:603px;top:1707px"><svg width="12" height="12" viewBox="0 0 12 12"><path d="M4 1l5 5-5 5" fill="none" stroke="#222" stroke-width="1.6"/></svg></div>
</section>

<section class="why">
  <h2 class="section-title" style="left:145px;top:1828px"><b>Why</b> Tenvora?</h2>
  <div class="rule" style="left:145px;top:1896px"></div>
  <div class="why-item" style="top:1923px"><span class="tick"><svg width="18" height="14" viewBox="0 0 18 14"><path d="M2 7l5 5 9-10" fill="none" stroke="#fff" stroke-width="3"/></svg></span>Fast Placement</div>
  <div class="why-item" style="top:2003px"><span class="tick"><svg width="18" height="14" viewBox="0 0 18 14"><path d="M2 7l5 5 9-10" fill="none" stroke="#fff" stroke-width="3"/></svg></span>Background Checked CDL Drivers</div>
  <div class="why-item" style="top:2084px"><span class="tick"><svg width="18" height="14" viewBox="0 0 18 14"><path d="M2 7l5 5 9-10" fill="none" stroke="#fff" stroke-width="3"/></svg></span>Coverage Across U.S.</div>
  <div class="why-item" style="top:2164px"><span class="tick"><svg width="18" height="14" viewBox="0 0 18 14"><path d="M2 7l5 5 9-10" fill="none" stroke="#fff" stroke-width="3"/></svg></span>24/7 Support</div>

  <div class="photo" role="img" aria-label="Delivery driver smiling behind the wheel of a van" style="left:715px;top:1844px;width:340px;height:213px;background:linear-gradient(135deg,#5b6770,#2f3a44 55%,#8a96a0)"></div>
  <div class="photo" role="img" aria-label="Driver in cap and uniform seated in a van cab" style="left:628px;top:1930px;width:215px;height:260px;border:4px solid #fff;background:linear-gradient(135deg,#3b4a5a,#1f2c3b 60%,#566575)"></div>
  <div class="photo" role="img" aria-label="Worker in a safety vest beside a white truck" style="left:854px;top:2069px;width:162px;height:167px;background:linear-gradient(135deg,#d9dcdd,#9da3a6 60%,#6e7477)"></div>
</section>

<section class="reviews" role="img" aria-label="Faded photo of truck drivers behind a green overlay"></section>
<h2 class="section-title" style="left:0;width:1200px;text-align:center;top:2422px;color:#fff"><b>Customer</b> Reviews</h2>
<div class="rule" style="left:568px;top:2476px;background:#bfe6d8"></div>

<div class="review" style="left:143px">
  <div class="ring"></div>
  <div class="card">
    <div class="quote">&ldquo;</div>
    <div class="stars">★★★★★</div>
    <p class="msg">“Lorem ipsum dolor sit amet, consectet ur adipisci ng elit, sed do eiusmod tempor incididunt ut labor e et dolore magna aliqua. Ut enim ad minim venia m, quis nostrud exercitation</p>
    <div class="name">John Doe</div>
    <div class="co">Company name</div>
  </div>
</div>
<div class="review" style="left:619px">
  <div class="ring"></div>
  <div class="card">
    <div class="quote">&ldquo;</div>
    <div class="stars">★★★★★</div>
    <p class="msg">“Lorem ipsum dolor sit amet, consectet ur adipisci ng elit, sed do eiusmod tempor incididunt ut labor e et dolore magna aliqua. Ut enim ad minim venia m, quis nostrud exercitation</p>
    <div class="name">John Doe</div>
    <div class="co">Company name</div>
  </div>
</div>
<svg class="abs" style="left:52px;top:2692px" width="44" height="28" viewBox="0 0 44 28"><path d="M42 14H4M16 2 4 14l12 12" fill="none" stroke="#fff" stroke-width="3"/></svg>
<svg class="abs" style="left:1104px;top:2692px" width="44" height="28" viewBox="0 0 44 28"><path d="M2 14h38M28 2l12 12-12 12" fill="none" stroke="#fff" stroke-width="3"/></svg>

<section class="contact">
  <h2 class="section-title" style="left:0;width:1200px;text-align:center;top:3094px"><b>Contact</b> Us</h2>
  <div class="rule" style="left:568px;top:3149px"></div>
  <div class="field" style="left:143px;top:3178px;width:289px;height:69px">Name</div>
  <div class="field" style="left:455px;top:3178px;width:288px;height:69px">Email</div>
  <div class="field" style="left:767px;top:3178px;width:288px;height:69px">Phone</div>
  <div class="field" style="left:143px;top:3265px;width:912px;height:159px;align-items:flex-start;padding-top:20px">Message</div>
  <div class="btn btn-green abs" style="left:484px;top:3444px;width:231px;height:67px;font-size:16px">SUBMIT NOW</div>
</section>

<footer class="site-footer">
  <div class="abs" style="left:1107px;top:24px;width:42px;height:42px;border-radius:50%;background:var(--green);display:flex;align-items:center;justify-content:center"><svg width="20" height="18" viewBox="0 0 20 18"><path d="M10 1C5 1 1 4 1 8c0 2 1 4 3 5l-1 4 5-3h2c5 0 9-3 9-6s-4-7-9-7z" fill="#fff"/></svg></div>
  <div class="brand"><span class="dot" style="background:#fff"></span>Tenvora</div>
  <nav class="foot-nav">HOME<i>/</i>SERVICES<i>/</i>ABOUT US<i>/</i>PRICING<i>/</i>CONTACT US</nav>
  <div class="foot-rule" style="top:185px"></div>

  <div class="foot-head" style="left:142px">Contact Info</div>
  <div class="foot-line" style="top:245px"><svg width="16" height="12" viewBox="0 0 16 12"><rect width="16" height="12" rx="1" fill="var(--green)"/><path d="M1 1l7 6 7-6" fill="none" stroke="#0b0b0b" stroke-width="1.4"/></svg>info@companyname.com</div>
  <div class="foot-line" style="top:286px"><svg width="15" height="15" viewBox="0 0 15 15"><path d="M3 1l3 3-2 2c1 2 3 4 5 5l2-2 3 3-2 2C6 14 1 9 1 3z" fill="var(--green)"/></svg>+1 888 888 8888</div>

  <div class="foot-head" style="left:463px">Follow Us</div>
  <div class="social" style="left:463px"></div>
  <div class="social" style="left:511px"></div>

  <div class="foot-head" style="left:632px">Subscribe To Our Newsletter</div>
  <div class="newsletter">Email address
    <svg class="abs" style="right:26px;top:19px" width="16" height="16" viewBox="0 0 16 16"><path d="M15 1 1 7l5 2 2 6z" fill="var(--green)"/></svg>
  </div>

  <div class="foot-rule" style="top:338px"></div>
  <div class="copyright">©&nbsp; Copyrights 2025 | All Rights Reserved</div>
</footer>

</body>
</html>
```